Bed Company needs business card

Hello, we are a bed company that makes specialized magnets for beds. We are an alternative healing company. I need a modern and upscale business card. Please incorporate my logo for the card.

Accepted file formats are AI, EPS, and Press-Ready PDFS.

Please include all fonts or convert them to outlines regardless of file type.

If you are designing the card in Photoshop the file Must be 1200dpi.

I am open to anything for the business card.  I really like all of your designs and if you want to change the color of the logo, you can.  I will be making the final selection by Friday.  Thank You for all of your designs.  Feel Free to submit different color logos if you want.  

Reason: I will make a decision Final on Friday April 20th. 2012. Good Luck and Thank you all for the designs.

Target Market(s)

My target Market is people, who are looking for alternative healing.

Industry/Entity Type

Business

Requirements
Must have
• My logo must be incorporated. The front card must have

Name
Job Title

Address
Work
Cell
Fax
email
web

Just put in fake info for the card.

The back of the card. I want the logo on the back with color. I just want it to look modern and cool.

```html
<!DOCTYPE html>
<html lang="en">
<head>
<meta charset="utf-8">
<title>Lodestone Rest — Business Card</title>
<link href="https://fonts.googleapis.com/css2?family=Source+Sans+3:wght@400;600;700&display=swap" rel="stylesheet">
<style>
  :root {
    --bg: #ebe6de;
    --card: #ffffff;
    --card-edge: #3a3a3a;
    --band: #136b3a;
    --brand: #2f8f42;
    --on-band: #ffffff;
    --divider: rgba(255,255,255,0.55);
  }
  * { box-sizing: border-box; margin: 0; padding: 0; }
  html, body {
    width: 1200px; height: 1061px; overflow: hidden;
    background: var(--bg);
    font-family: "Source Sans 3", "Myriad Pro", Arial, sans-serif;
  }
  .canvas { position: relative; width: 1200px; height: 1061px; }

  .card {
    position: absolute;
    width: 739px; height: 422px;
    background: var(--card);
    border: 1.5px solid var(--card-edge);
    border-radius: 28px;
    overflow: hidden;
  }
  .card--front { left: 103px; top: 67px; }
  .card--back  { left: 379px; top: 542px; }

  .brand {
    position: absolute;
    display: flex; align-items: center; gap: 18px;
    color: var(--brand);
    font-weight: 700;
    white-space: nowrap;
  }
  .brand__mark { background: var(--brand); flex: none; }
  .card--front .brand { left: 143px; top: 118px; font-size: 58px; }
  .card--front .brand__mark { width: 58px; height: 58px; }
  .card--back .brand { left: 112px; top: 160px; font-size: 64px; }
  .card--back .brand__mark { width: 64px; height: 64px; }

  .rule {
    position: absolute; left: 0; right: 0; top: 226px;
    height: 3px; background: var(--band);
  }
  .band {
    position: absolute; left: 0; right: 0; top: 234px; bottom: 0;
    background: var(--band);
    color: var(--on-band);
  }

  .identity {
    position: absolute; right: 410px; top: 36px;
    text-align: right;
  }
  .identity__name { font-size: 22px; font-weight: 700; line-height: 1; }
  .identity__title { font-size: 17px; margin-top: 8px; line-height: 1; }
  .identity__address { font-size: 17px; line-height: 25px; margin-top: 22px; }

  .divider {
    position: absolute; left: 362px; top: 19px;
    width: 1.5px; height: 136px; background: var(--divider);
  }

  .contacts {
    position: absolute; left: 390px; top: 34px;
    list-style: none;
    font-size: 18px;
  }
  .contacts li {
    display: flex; align-items: center; gap: 10px;
    height: 31px; line-height: 1;
  }
  .contacts svg { width: 14px; height: 14px; flex: none; fill: var(--on-band); }
</style>
</head>
<body>
<main class="canvas">

  <section class="card card--front" aria-label="Business card front">
    <div class="brand">
      <span class="brand__mark"></span>
      <span class="brand__name">Lodestone Rest</span>
    </div>
    <div class="rule"></div>
    <div class="band">
      <div class="identity">
        <p class="identity__name">Your Name</p>
        <p class="identity__title">Title</p>
        <p class="identity__address">Complex Name, Street Name,<br>Area, City Name,000 000</p>
      </div>
      <div class="divider"></div>
      <ul class="contacts">
        <li>
          <svg viewBox="0 0 16 16" aria-hidden="true"><path d="M3.5 1.5l2.5 0 1.2 3.2-1.6 1.2c.8 1.8 2.3 3.3 4.1 4.1l1.2-1.6 3.2 1.2v2.5c0 .8-.7 1.4-1.5 1.4C6.6 13.5 2.5 9.4 2.1 3c0-.8.6-1.5 1.4-1.5z"/></svg>
          <span>+91 98765 43210</span>
        </li>
        <li>
          <svg viewBox="0 0 16 16" aria-hidden="true"><path d="M4.5 1h7c.6 0 1 .4 1 1v12c0 .6-.4 1-1 1h-7c-.6 0-1-.4-1-1V2c0-.6.4-1 1-1zm1 2v7h5V3h-5zm2.5 8.5a1 1 0 100 2 1 1 0 000-2z"/></svg>
          <span>+91 98765 43210</span>
        </li>
        <li>
          <svg viewBox="0 0 16 16" aria-hidden="true"><path d="M1 3.5h14v1L8 9 1 4.5zM1 6l7 4.5L15 6v6.5H1z"/></svg>
          <span>hello@lodestonerest.in</span>
        </li>
        <li>
          <svg viewBox="0 0 16 16" aria-hidden="true"><path d="M8 1a7 7 0 100 14A7 7 0 008 1zm0 1.5c.8 0 1.7 1.6 2 4H6c.3-2.4 1.2-4 2-4zM5.9 3a8.6 8.6 0 00-1.3 3.5H2.6A5.5 5.5 0 015.9 3zm4.2 0a5.5 5.5 0 013.3 3.5h-2A8.6 8.6 0 0010.1 3zM2.6 8h2c.1 1.4.5 2.7 1.3 3.5A5.5 5.5 0 012.6 8zm3.4 0h4c-.3 2.4-1.2 4-2 4s-1.7-1.6-2-4zm5.4 0h2a5.5 5.5 0 01-3.3 3.5c.8-.8 1.2-2.1 1.3-3.5z"/></svg>
          <span>http://www.lodestonerest.com</span>
        </li>
      </ul>
    </div>
  </section>

  <section class="card card--back" aria-label="Business card back">
    <div class="brand">
      <span class="brand__mark"></span>
      <span class="brand__name">Lodestone Rest</span>
    </div>
  </section>

</main>
</body>
</html>
```